Print design needed to improve the layout and look of some existing documents

We need someone to take a couple of existing documents that we have and make them look much better using our existing logo and corporate colors etc. We require these to be delivered in a format that will allow our staff to edit the content as necessary via Microsoft word for conversion once finalized into a PDF. Ideally, we will also be able to use this as a newsletter template or for other documents that might be required in our business. www.calderfinch.com.au
Updates

Project Deadline Extended Reason: So far, I have only seen one design that I believe is quite good quality. Added Sunday, July 3, 2016

Target Market(s)

Business owners, executives, retirees

Industry/Entity Type

Financial Service

Font styles to use
Serif

Requirements
Must have
• Design that uses our existing branding and colors. It also needs to be ina form that we can edit the content / update easily. Ideally the format / layout could also be used for other documents such as short newsletters etc.
Nice to have
• Fresh, simple and crisp. Very professional looking.
Should not have
• strange fonts, weird layouts.

```html
<!DOCTYPE html>
<html lang="en">
<head>
<meta charset="utf-8">
<title>Calder Finch Privacy Policy</title>
<link rel="stylesheet" href="https://fonts.googleapis.com/css2?family=Didact+Gothic&family=Mulish:wght@600;700&display=swap">
<style>
  :root {
    --backdrop: #bec1c6;
    --paper: #ffffff;
    --brand-blue: #14a9e1;
    --brand-green: #8dc63f;
    --ink: #4a4a4a;
    --ink-soft: #5b5b5b;
    --photo: #595959;
    --rule-grey: #5a5a5a;
  }
  html, body {
    margin: 0;
    width: 1200px;
    height: 800px;
    overflow: hidden;
    background: var(--backdrop);
  }
  .page {
    position: absolute;
    top: 86px;
    width: 456px;
    height: 591px;
    background: var(--paper);
    box-shadow: 0 2px 6px rgba(0,0,0,0.25);
    font-family: "Didact Gothic", sans-serif;
    color: var(--ink);
  }
  .page--cover { left: 148px; }
  .page--content { left: 614px; }

  .cover-bar { position: absolute; left: 27px; width: 406px; height: 3px; }
  .cover-bar--blue { background: var(--brand-blue); }
  .cover-bar--green { background: var(--brand-green); }
  .cover-photo { position: absolute; left: 27px; width: 406px; background: var(--photo); }

  .brand-name {
    font-family: "Mulish", sans-serif;
    font-weight: 600;
    color: var(--ink);
    letter-spacing: 0.5px;
    display: flex;
    align-items: center;
    gap: 7px;
  }
  .brand-mark { width: 10px; height: 10px; border-radius: 50%; background: var(--brand-blue); }

  .cover-brand { position: absolute; top: 214px; left: 0; right: 0; justify-content: center; font-size: 26px; }
  .cover-title {
    position: absolute; top: 256px; left: 0; right: 0; margin: 0;
    text-align: center; font-family: "Mulish", sans-serif; font-weight: 700;
    font-size: 15.5px; color: var(--ink);
  }
  .cover-intro {
    position: absolute; top: 280px; left: 30px; right: 30px; margin: 0;
    text-align: center; font-size: 7.2px; line-height: 10.2px; color: var(--ink-soft);
  }

  .content-brand { position: absolute; top: 22px; left: 33px; font-size: 18px; }

  .column { position: absolute; width: 186px; }
  .column--left { left: 37px; }
  .column--right { left: 244px; }

  .section-bar { height: 4px; width: 100%; }
  .section-bar--blue { background: var(--brand-blue); }
  .section-bar--grey { background: var(--rule-grey); }
  .section-heading {
    margin: 7px 0 8px; font-family: "Mulish", sans-serif; font-weight: 600;
    font-size: 8.2px; line-height: 11.5px;
  }
  .section-heading--blue { color: var(--brand-blue); }
  .section-heading--dark { color: var(--ink); text-align: justify; }
  .section-text {
    margin: 0 0 7px; font-size: 6.3px; line-height: 9.2px;
    text-align: justify; color: var(--ink-soft);
  }
  .column--right .section-text { text-align: left; }

  .closing-rule { position: absolute; top: 534px; left: 33px; width: 405px; height: 2px; background: var(--rule-grey); }
</style>
</head>
<body>

<section class="page page--cover">
  <div class="cover-bar cover-bar--blue" style="top:20px"></div>
  <div class="cover-photo" style="top:24px;height:174px" role="img" aria-label="Cover photograph"></div>
  <div class="cover-bar cover-bar--green" style="top:199px"></div>

  <div class="brand-name cover-brand"><span class="brand-mark"></span>CALDER FINCH</div>
  <h1 class="cover-title">Calder Finch Pty Ltd Privacy Policy</h1>
  <p class="cover-intro">We are committed to protecting your privacy in accordance with the <em>Privacy Act 1988</em> (Cth). This Policy describes our current policies and practices in relation to the collection, handling, use and disclosure of personal information. It also deals with how you can complain about a breach of the privacy laws, how you can access the personal information we hold about you and how to have that information corrected.</p>

  <div class="cover-bar cover-bar--green" style="top:344px"></div>
  <div class="cover-photo" style="top:348px;height:202px" role="img" aria-label="Secondary cover photograph"></div>
  <div class="cover-bar cover-bar--blue" style="top:551px"></div>
</section>

<section class="page page--content">
  <div class="brand-name content-brand"><span class="brand-mark"></span>CALDER FINCH</div>

  <div class="column column--left" style="top:62px">
    <div class="section-bar section-bar--blue"></div>
    <h2 class="section-heading section-heading--blue">What information do we collect and how do we use it?</h2>
    <p class="section-text">If you are acquiring or have acquired a service from Calder Finch Pty Ltd, we collect and hold your personal information for the purpose of providing you with relevant and accurate service and financial advice as well as managing and administering the service. This can include a broad range of information ranging from your name, postal and email address, date of birth, contact details and age to other information about your personal affairs including your financial details, tax file numbers or other information the organisation considers necessary.</p>
    <p class="section-text">We may disclose the information that you provide to third party organisations where you have request that we liaise with or refer you to the organisations. This may include firms providing accounting, legal, credit, transactional banking, investment administration or insurance services.</p>
    <p class="section-text">We may use your information to enable us to manage your ongoing requirements and our relationship with you. We may do so by mail or electronically unless you tell us that you do not wish to receive electronic communications.</p>
    <p class="section-text">From time to time we may use your contact details to send you offers, updates, events, articles, newsletters or other information about services or events that we believe will be of interest to you. You can contact us at any time if you no longer wish us to do so.</p>
    <p class="section-text">We may also use your information internally to help us improve our services and help resolve any problems.</p>
  </div>

  <div class="column column--left" style="top:446px">
    <div class="section-bar section-bar--blue"></div>
    <h2 class="section-heading section-heading--blue">What if you don't provide some information to us?</h2>
    <p class="section-text">If you do not provide us with some or all of the information that we ask for, we may not be able to accurately assess your situation and provide relevant and accurate financial advice.</p>
  </div>

  <div class="column column--right" style="top:62px">
    <div class="section-bar section-bar--grey"></div>
    <h2 class="section-heading section-heading--dark">How do we hold and protect your information?</h2>
    <p class="section-text">We strive to maintain the relevance, reliability, accuracy, completeness and currency of the personal information we hold and to protect its privacy and security. We keep personal information only for as long as is reasonably necessary for the purpose for which it was collected or to comply with any applicable legal or ethical reporting or document retention requirements.</p>
    <p class="section-text">We store information collected from you in different ways, including in paper and electronic form. The security of your personal information is important to us and we take reasonable steps to protect it from misuse and loss and unauthorised access, modification or disclosure.</p>
  </div>

  <div class="column column--right" style="top:250px">
    <div class="section-bar section-bar--grey"></div>
    <h2 class="section-heading section-heading--dark">Will we disclose the information we collect to anyone?</h2>
    <p class="section-text">We do not sell, trade, or rent your personal information to others. We may disclose your information to third party organisations where you have request that we liaise with or refer you to the organisations. This may include firms providing investment, superannuation, accounting legal, credit, transactional banking or insurance services and may need to provide your information to contractors who supply services to us or to other companies in the event of a corporate sale, merger, reorganisation, dissolution or similar event. However, we will take all reasonable steps to ensure that they protect your information in the same way that we do.</p>
    <p class="section-text">We may also provide your information to others if we are required to do so by law or under some unusual other circumstances which the Privacy Act permits. We will not provide your information to any overseas recipients unless we are required to by Law.</p>
  </div>

  <div class="closing-rule"></div>
</section>

</body>
</html>
```